Website that informs user about the Darknet

A short 1 pager website that explains what the darknet is.
Current site: https://velmora.gs/ & https://quintable.kr/. No logo needed. Just an informational page. Choose the layout / colours that you prefer.

Target Market(s)

Endusers, companies etc.

Coding

Coded - Design and coding required

Number of Pages Required

1 page

Requirements
Must have
• 1 Small contact form - thats all
Should not have
• The page must look professional. Not for kids. I target mainly adults / employees

```html
<!DOCTYPE html>
<html lang="en">
<head>
<meta charset="utf-8">
<title>Velmora – Darknet and Dark Web</title>
<link href="https://fonts.googleapis.com/css2?family=Jost:wght@500;600;700&family=Roboto:wght@400;500;700&display=swap" rel="stylesheet">
<style>
:root{
  --black:#000;
  --ink:#050608;
  --panel:#101113;
  --panel-2:#0b0d10;
  --field:#0f1012;
  --white:#fff;
  --muted:#d6d8dc;
  --blue:#0b58b8;
  --blue-bright:#1a6fd6;
  --link:#2b78d6;
  --teal:#2e8cc2;
  --line:#2a2c30;
}
*{box-sizing:border-box;margin:0;padding:0}
html,body{width:1200px;height:4088px;overflow:hidden;background:var(--black)}
body{font-family:"Roboto",sans-serif;color:var(--white);position:relative}
.abs{position:absolute}
h1,h2,h3,.logo{font-family:"Jost",sans-serif}
.logo{font-weight:700;font-size:44px;letter-spacing:0.5px;color:var(--white)}

/* header */
.top-line{left:0;top:0;width:1200px;height:5px;background:var(--blue)}
.site-header{left:0;top:5px;width:1200px;height:95px;background:var(--black)}
.site-header .logo{left:110px;top:22px}
.nav{left:582px;top:38px;font-size:15px}
.nav a{color:var(--white);text-decoration:none;position:absolute;white-space:nowrap}
.nav a.active{color:var(--blue-bright);border-bottom:2px solid var(--blue-bright);padding-bottom:4px}
.btn-login{left:968px;top:27px;width:121px;height:45px;background:var(--blue);border-radius:3px;font-weight:700;font-size:15px;display:flex;align-items:center;justify-content:center;gap:10px}

/* hero */
.hero{left:0;top:100px;width:1200px;height:840px;background:
  radial-gradient(ellipse 420px 360px at 900px 260px,#1f3a44 0%,rgba(16,30,38,0) 70%),
  linear-gradient(135deg,#1c3a45 0%,#0f2a35 35%,#0a1820 65%,#060b10 100%)}
.hero-title{left:100px;top:258px;width:500px;text-align:center;font-size:64px;font-weight:700;line-height:72px;letter-spacing:-0.5px;white-space:nowrap}
.btn{display:flex;align-items:center;justify-content:center;gap:10px;font-weight:700;color:var(--white);font-size:15px}
.btn-start{left:270px;top:437px;width:155px;height:54px;background:var(--blue);border-radius:3px}
.slider-dots{left:1059px;top:320px}
.slider-dots span{position:absolute;left:0;width:12px;height:12px;border-radius:50%;background:var(--white)}
.slider-dots span.on{background:transparent;border:2px solid var(--white)}
.slider-dots span.on::after{content:"";position:absolute;left:2px;top:2px;width:4px;height:4px;border-radius:50%;background:var(--white)}
.hero-wave{left:0;top:740px}

.side-orb{left:-80px;top:952px;width:163px;height:163px;border-radius:50%;background:#07162a}

/* section headings */
.section-title{width:1200px;left:0;text-align:center;font-size:30px;font-weight:600;letter-spacing:0.2px}
.section-title::after{content:"";display:block;width:56px;height:4px;background:var(--white);margin:10px auto 0;border-radius:2px}

/* understand */
.info-card{width:254px;height:344px;text-align:center}
.info-card.featured{background:var(--panel)}
.icon-ring{position:absolute;left:73px;width:108px;height:108px;border-radius:50%;background:#0a2440;display:flex;align-items:center;justify-content:center}
.icon-ring i{width:74px;height:74px;border-radius:50%;background:#0c3a6e;display:flex;align-items:center;justify-content:center}
.info-card h3{position:absolute;left:0;width:254px;font-family:"Roboto",sans-serif;font-size:14px;font-weight:700;color:var(--white)}
.info-card p{position:absolute;left:14px;width:226px;font-size:12.5px;line-height:24px;color:var(--muted)}
.read-more{position:absolute;left:0;width:254px;display:flex;justify-content:center;align-items:center;gap:10px;color:var(--link);font-size:15px;font-weight:700}

/* monitored */
.monitor{left:0;top:1543px;width:1200px;height:695px;background:linear-gradient(180deg,#0c0e12,#0a0c0f)}
.monitor-lead{left:165px;top:142px;width:885px;text-align:center;font-size:15px;line-height:26px;color:var(--muted)}
.monitor-text{left:127px;top:284px;width:445px;font-size:15px;line-height:25.8px;text-align:justify;color:var(--muted)}
.btn-learn{left:127px;top:536px;width:163px;height:53px;background:var(--teal);border-radius:2px}
.monitor-frame{left:616px;top:298px;width:467px;height:298px;border-left:3px solid var(--teal);border-bottom:3px solid var(--teal);border-radius:0 0 0 4px}
.monitor-img{left:628px;top:288px;width:461px;height:296px;background:linear-gradient(160deg,#0b1a12 0%,#153a22 35%,#0d1f16 60%,#2a2d33 100%)}

/* accessing */
.access-card{top:2401px;width:303px;height:416px;border-radius:18px;background:var(--panel);overflow:hidden}
.access-card.featured{border-bottom:3px solid var(--blue-bright)}
.access-img{position:absolute;left:4px;top:5px;width:295px;height:188px;border-radius:14px 14px 0 0}
.access-card h3{position:absolute;left:21px;top:214px;font-size:16px;font-weight:600;white-space:nowrap}
.access-card .bar{position:absolute;left:21px;top:248px;width:38px;height:2px;background:var(--white)}
.access-card p{position:absolute;left:21px;top:264px;width:266px;font-size:13.5px;line-height:23px;color:var(--muted)}
.access-card p.just{text-align:justify}
.arrow-btn{position:absolute;left:21px;top:356px;width:40px;height:40px;border:2px solid var(--white);border-radius:50%;display:flex;align-items:center;justify-content:center}
.btn-small{position:absolute;left:21px;top:358px;width:137px;height:36px;background:var(--teal);border-radius:2px;font-size:14px}

/* contact form */
.form-zone{left:0;top:2905px;width:1200px;height:640px;background:linear-gradient(180deg,#0c0d10,#08090b)}
.field{background:var(--field);font-size:15px;color:var(--white);padding:0 24px;display:flex;align-items:center}
.field.area{align-items:flex-start;padding-top:22px}
.submit{left:111px;top:3392px;width:978px;height:52px;background:var(--field);font-weight:700;font-size:15px;display:flex;align-items:center;justify-content:center}

/* footer */
.footer-wave{left:0;top:3480px}
.site-footer .logo{left:111px;top:3728px}
.footer-about{left:111px;top:3806px;width:250px;font-size:14.5px;line-height:27px;text-align:justify;color:var(--muted)}
.footer-head{font-family:"Jost",sans-serif;font-weight:600;font-size:16px}
.footer-head::after{content:"";display:block;width:45px;height:3px;background:var(--blue-bright);margin-top:8px}
.quick a{position:absolute;left:463px;color:var(--white);text-decoration:none;font-size:15px}
.dot-icon{width:34px;height:34px;border-radius:50%;background:#1a1b1e;display:flex;align-items:center;justify-content:center}
.contact-line{font-size:15px;line-height:24px}
.footer-rule{left:111px;top:4012px;width:978px;height:1px;background:#3a3c40}
.copyright{left:0;top:4034px;width:1200px;text-align:center;font-size:13px;color:var(--muted)}
</style>
</head>
<body>

<!-- header -->
<div class="abs top-line"></div>
<header class="abs site-header">
  <div class="abs logo">VELMORA</div>
  <nav class="abs nav">
    <a class="active" style="left:0">HOME</a>
    <a style="left:78px">ABOUT US</a>
    <a style="left:184px">START</a>
    <a style="left:265px">CONTACT US</a>
  </nav>
  <div class="abs btn btn-login">LOGIN
    <svg width="12" height="14" viewBox="0 0 12 14"><rect x="1" y="6" width="10" height="8" rx="1" fill="#fff"/><path d="M3 6V4a3 3 0 0 1 6 0v2" stroke="#fff" stroke-width="2" fill="none"/></svg>
  </div>
</header>

<!-- hero -->
<section class="abs hero" role="img" aria-label="Hooded person typing in front of monitors showing code and a world map, in teal and dark tones">
  <h1 class="abs hero-title">DARKNET AND<br>DARK WEB</h1>
  <div class="abs btn btn-start">GET STARTED
    <svg width="14" height="14" viewBox="0 0 14 14"><circle cx="7" cy="7" r="7" fill="#fff"/><path d="M5.5 4l3 3-3 3" stroke="#0b58b8" stroke-width="1.8" fill="none"/></svg>
  </div>
  <div class="abs slider-dots">
    <span style="top:0"></span><span style="top:25px"></span><span class="on" style="top:51px"></span><span style="top:77px"></span><span style="top:103px"></span>
  </div>
</section>
<svg class="abs hero-wave" width="1200" height="210" viewBox="0 0 1200 210">
  <path d="M0 118 C120 60 260 30 420 55 C620 90 820 210 1000 188 C1090 176 1160 150 1200 130 L1200 210 L0 210 Z" fill="#000"/>
  <path d="M0 118 C120 60 260 30 420 55 C620 90 820 210 1000 188 C1090 176 1160 150 1200 130" stroke="#0b58b8" stroke-width="6" fill="none"/>
</svg>
<div class="abs side-orb"></div>

<!-- understand -->
<h2 class="abs section-title" style="top:988px">UNDERSTAND THE DARKNET</h2>

<article class="abs info-card" style="left:38px;top:1106px">
  <div class="icon-ring" style="top:30px"><i><svg width="34" height="34" viewBox="0 0 34 34"><circle cx="17" cy="11" r="7" fill="#5ea6f0"/><path d="M4 33c0-8 6-13 13-13s13 5 13 13z" fill="#5ea6f0"/></svg></i></div>
  <h3 style="top:162px">INTRODUCTION</h3>
  <p style="top:204px">The Dark Web is part of the Internet that cannot be indexed by regular search engines.</p>
  <div class="read-more" style="top:292px">Read More <svg width="14" height="14"><circle cx="7" cy="7" r="7" fill="#2b78d6"/><path d="M5.5 4l3 3-3 3" stroke="#000" stroke-width="1.8" fill="none"/></svg></div>
</article>

<article class="abs info-card" style="left:316px;top:1106px">
  <div class="icon-ring" style="top:30px"><i><svg width="34" height="34" viewBox="0 0 34 34"><rect x="7" y="15" width="18" height="15" rx="2" fill="#5ea6f0"/><path d="M10 15V10a6 6 0 0 1 12 0v5" stroke="#5ea6f0" stroke-width="3" fill="none"/></svg></i></div>
  <h3 style="top:162px">UNDERSTAND THE INTERNET</h3>
  <p style="top:204px">The Internet is a network of computers that are linked together via a worldwide network. When someone sets</p>
  <div class="read-more" style="top:292px">Read More <svg width="14" height="14"><circle cx="7" cy="7" r="7" fill="#2b78d6"/><path d="M5.5 4l3 3-3 3" stroke="#000" stroke-width="1.8" fill="none"/></svg></div>
</article>

<article class="abs info-card featured" style="left:616px;top:1106px">
  <div class="icon-ring" style="top:27px"><i><svg width="34" height="34" viewBox="0 0 34 34"><rect x="6" y="6" width="22" height="22" rx="3" stroke="#5ea6f0" stroke-width="2.5" fill="none"/><circle cx="17" cy="17" r="5" fill="#5ea6f0"/></svg></i></div>
  <h3 style="top:157px">DARKNET VS. INTERNET</h3>
  <p style="top:199px">Unlike the Internet, however, you can't access the websites with a regular web browser,example</p>
  <div class="read-more" style="top:287px">Read More <svg width="14" height="14"><circle cx="7" cy="7" r="7" fill="#2b78d6"/><path d="M5.5 4l3 3-3 3" stroke="#000" stroke-width="1.8" fill="none"/></svg></div>
</article>

<article class="abs info-card" style="left:895px;top:1106px">
  <div class="icon-ring" style="top:30px"><i><svg width="34" height="34" viewBox="0 0 34 34"><circle cx="17" cy="17" r="11" stroke="#5ea6f0" stroke-width="3" fill="none"/><rect x="12" y="15" width="10" height="8" fill="#5ea6f0"/><path d="M14 15v-2a3 3 0 0 1 6 0v2" stroke="#5ea6f0" stroke-width="2" fill="none"/></svg></i></div>
  <h3 style="top:162px">IS THE DARKNET ILLEGAL?</h3>
  <p style="top:204px">Many think the darknet and access is crinimell. But this is not the case. The idea of the darknet comes.</p>
  <div class="read-more" style="top:292px">Read More <svg width="14" height="14"><circle cx="7" cy="7" r="7" fill="#2b78d6"/><path d="M5.5 4l3 3-3 3" stroke="#000" stroke-width="1.8" fill="none"/></svg></div>
</article>

<!-- monitored -->
<section class="abs monitor">
  <h2 class="abs section-title" style="top:70px;font-size:28px">WHY AND HOW CAN THE DARKNET BE MONITORED?</h2>
  <p class="abs monitor-lead">The dark web can be a scary place. Especially if you're new to it and are not properly equipped with all you need to scour safely. Dark web monitoring refers to the process by which you can search, track, or monitor the information regarding your organization on the dark web. With the right tools on the dark web, you can track lost, stolen, or leaked information such as intellectual property, compromised passwords, breached credentials, leaked organization's sensitive data, etc.</p>
  <p class="abs monitor-text">Oftentimes, these sensitive information are usually transacted among unscrupulous characters in the dark web. With proper dark web monitoring tools, you can better detect threats and dangers on the dark web. Which is a step further than just anti-virus, anti-malware programs, and programs that help in identity theft monitoring. In the case of these anti-malware and antivirus programs, they help you monitor and prevent any malicious code aimed at stealing information. However, they do very little in situations, where the deed has already been done.</p>
  <div class="abs btn btn-learn">LEARN MORE <svg width="14" height="14"><circle cx="7" cy="7" r="7" fill="#fff"/><path d="M5.5 4l3 3-3 3" stroke="#2e8cc2" stroke-width="1.8" fill="none"/></svg></div>
  <div class="abs monitor-frame"></div>
  <div class="abs monitor-img" role="img" aria-label="Computer screen with green security dashboards, a keyboard and mouse on a desk"></div>
</section>

<!-- accessing -->
<h2 class="abs section-title" style="top:2313px">ACCESSING THE DARKNET</h2>

<article class="abs access-card" style="left:127px">
  <div class="access-img" role="img" aria-label="Hands typing on a laptop with a glowing padlock overlay" style="background:linear-gradient(150deg,#2f4c66,#6d7f90 50%,#1b2733)"></div>
  <h3>Relay Browser</h3><div class="bar"></div>
  <p class="just">Accessing the dark web can be done using a special browser called Relay. The Relay Browser is a web broswer that</p>
  <div class="arrow-btn"><svg width="18" height="12"><path d="M1 6h15M11 1l5 5-5 5" stroke="#fff" stroke-width="2" fill="none"/></svg></div>
</article>

<article class="abs access-card featured" style="left:455px">
  <div class="access-img" role="img" aria-label="Hands on a backlit keyboard with a blue shield and lock graphic" style="background:linear-gradient(150deg,#0d3e78,#1a5fa6 45%,#0a1c33)"></div>
  <h3>Proxies - Example veilgate.ws</h3><div class="bar"></div>
  <p>Veilgate.ws is a darknet gateway or Relay2 Web proxy. Simply replace .onion with veilgate.ws in your webbrowser</p>
  <div class="btn btn-small">Learn More <svg width="13" height="13"><circle cx="6.5" cy="6.5" r="6.5" fill="#fff"/><path d="M5 3.5l3 3-3 3" stroke="#2e8cc2" stroke-width="1.7" fill="none"/></svg></div>
</article>

<article class="abs access-card" style="left:784px">
  <div class="access-img" role="img" aria-label="Hand on a keyboard in front of glowing blue binary digits" style="background:linear-gradient(150deg,#174a6e,#2d7aa8 45%,#0c2233)"></div>
  <h3>Browser Extension</h3><div class="bar"></div>
  <p>Lorem ipsum dolor consectetur elited sed do eiusmod tempor incididunt utet labored eted dolore magna aliqua.</p>
  <div class="arrow-btn"><svg width="18" height="12"><path d="M1 6h15M11 1l5 5-5 5" stroke="#fff" stroke-width="2" fill="none"/></svg></div>
</article>

<!-- contact form -->
<section class="abs form-zone"></section>
<h2 class="abs section-title" style="top:2964px">WANT TO KNOW MORE?</h2>
<form>
  <div class="abs field area" style="left:111px;top:3050px;width:476px;height:302px">Message*</div>
  <div class="abs field" style="left:616px;top:3050px;width:473px;height:54px">First Name*</div>
  <div class="abs field" style="left:616px;top:3133px;width:473px;height:54px">Last Name*</div>
  <div class="abs field" style="left:616px;top:3215px;width:473px;height:54px">Email*</div>
  <div class="abs field" style="left:616px;top:3298px;width:473px;height:54px">Address*</div>
  <div class="abs submit">SUBMIT NOW</div>
</form>

<svg class="abs footer-wave" width="1200" height="240" viewBox="0 0 1200 240">
  <path d="M0 108 C120 60 260 40 400 60 C600 90 780 190 940 188 C1060 186 1140 150 1200 120 L1200 240 L0 240 Z" fill="#000"/>
  <path d="M0 100 C120 52 260 34 400 54 C600 84 780 178 940 176 C1060 174 1140 140 1200 112" stroke="#1e2024" stroke-width="18" fill="none"/>
  <path d="M0 108 C120 60 260 40 400 60 C600 90 780 190 940 188 C1060 186 1140 150 1200 120" stroke="#0b58b8" stroke-width="5" fill="none"/>
</svg>

<!-- footer -->
<footer class="site-footer">
  <div class="abs logo">VELMORA</div>
  <p class="abs footer-about">The Dark Web is also referred to as the Darknet. Both terms stand for the same concept. To understand the darknet, we must first explain the Internet.</p>

  <div class="abs footer-head" style="left:463px;top:3730px">QUICK LINKS</div>
  <div class="quick">
    <a style="top:3788px">+&nbsp;&nbsp;Home</a>
    <a style="top:3829px">+&nbsp;&nbsp;About us</a>
    <a style="top:3870px">+&nbsp;&nbsp;Start</a>
    <a style="top:3911px">+&nbsp;&nbsp;Contact us</a>
  </div>

  <div class="abs footer-head" style="left:659px;top:3730px">CONTACT US</div>
  <div class="abs dot-icon" style="left:655px;top:3795px"><svg width="12" height="16"><path d="M6 1a5 5 0 0 1 5 5c0 4-5 9-5 9S1 10 1 6a5 5 0 0 1 5-5z" fill="#fff"/><circle cx="6" cy="6" r="2" fill="#1a1b1e"/></svg></div>
  <div class="abs contact-line" style="left:703px;top:3788px">616Lorem ipsum dolor<br>consectetur adipiscing</div>
  <div class="abs dot-icon" style="left:655px;top:3865px"><svg width="14" height="14" viewBox="0 0 14 14"><path d="M3 1l3 3-2 2c1 2 2 3 4 4l2-2 3 3-2 2C6 13 1 8 1 3z" fill="#fff"/></svg></div>
  <div class="abs contact-line" style="left:703px;top:3857px">Call Us<br>+1 555 010 0199</div>
  <div class="abs dot-icon" style="left:655px;top:3933px"><svg width="14" height="10"><rect x="0" y="0" width="14" height="10" rx="1" fill="#fff"/><path d="M0 0l7 6 7-6" stroke="#1a1b1e" stroke-width="1.5" fill="none"/></svg></div>
  <div class="abs contact-line" style="left:703px;top:3925px">Email us<br>info@velmora.gs</div>

  <div class="abs footer-head" style="left:952px;top:3730px">FOLLOW US</div>
  <div class="abs dot-icon" style="left:951px;top:3795px"></div>
  <div class="abs contact-line" style="left:1000px;top:3788px">Like us on<br>FRIENDLINE</div>
  <div class="abs dot-icon" style="left:951px;top:3863px"></div>
  <div class="abs contact-line" style="left:1000px;top:3855px">Follow us on<br>CHIRPNET</div>
  <div class="abs dot-icon" style="left:951px;top:3930px"></div>
  <div class="abs contact-line" style="left:1000px;top:3922px">Follow us on<br>WORKLINK</div>

  <div class="abs footer-rule"></div>
  <div class="abs copyright">© 2022 Copyrights &nbsp;Velmora All Rights Reserved.</div>
</footer>

</body>
</html>
```